Heronby Mortgage Capital Business Card

We need a business card design for our mortgage servicing company. In addition to servicing the loans of homeowners, we help homeowners with purchasing their homes and any mortgage refinancing. We would like to see designs that use the colors in the logo attached below (gold-ish yellow and navy blue), and any other design you deem fit! The design should communicate a simpler life with smart mortgages provided by Heronby.

```html
<!DOCTYPE html>
<html lang="en">
<head>
<meta charset="utf-8">
<title>Heronby Mortgage Capital – Business Card</title>
<link rel="stylesheet" href="https://fonts.googleapis.com/css2?family=Crimson+Text:wght@400;700&display=swap">
<style>
  :root {
    --navy: #281f55;
    --gold: #dca92f;
    --ink: #3a3a44;
    --paper: #ffffff;
    --backdrop: #e4e5e8;
  }
  * { box-sizing: border-box; margin: 0; padding: 0; }
  html, body {
    width: 1200px;
    height: 800px;
    overflow: hidden;
    background: var(--backdrop);
    font-family: "Crimson Text", Georgia, serif;
  }
  .sheet {
    width: 1200px;
    height: 800px;
    display: flex;
    align-items: center;
    justify-content: center;
    gap: 60px;
  }
  .card {
    position: relative;
    width: 520px;
    height: 300px;
    box-shadow: 0 6px 18px rgba(0,0,0,0.12);
  }
  .card--back { background: var(--navy); }
  .card--front { background: var(--paper); color: var(--ink); }

  .wordmark {
    position: absolute;
    left: 50%;
    top: 50%;
    transform: translate(-50%, -50%);
    font-weight: 700;
    font-size: 46px;
    line-height: 1;
    color: var(--gold);
    white-space: nowrap;
    letter-spacing: 0.5px;
  }
  .card--front .wordmark { top: 44%; }

  .holder {
    position: absolute;
    left: 28px;
    top: 24px;
  }
  .holder__line {
    font-size: 17px;
    line-height: 1.15;
  }
  .holder__name {
    color: var(--gold);
    text-transform: uppercase;
    letter-spacing: 0.5px;
  }
  .holder__divider { color: var(--gold); margin: 0 4px; }
  .holder__role { color: var(--ink); }
  .holder__phone {
    display: flex;
    align-items: center;
    gap: 6px;
    font-size: 15px;
    margin-top: 2px;
  }

  .contact {
    position: absolute;
    right: 26px;
    bottom: 24px;
    list-style: none;
    text-align: right;
  }
  .contact__item {
    display: flex;
    align-items: center;
    justify-content: flex-end;
    gap: 7px;
    font-size: 15px;
    line-height: 1.35;
  }
  .icon { width: 13px; height: 13px; flex: none; fill: var(--navy); }
</style>
</head>
<body>
<main class="sheet">
  <section class="card card--back" aria-label="Card back">
    <div class="wordmark">Heronby Mortgage</div>
  </section>

  <section class="card card--front" aria-label="Card front">
    <div class="holder">
      <p class="holder__line">
        <span class="holder__name">Avery Dalton</span><span class="holder__divider">|</span><span class="holder__role">Director</span>
      </p>
      <p class="holder__phone">
        <svg class="icon" viewBox="0 0 16 16" aria-hidden="true"><path d="M3.6 1.2l2.3 2.6-1.3 1.7c.9 2 2.4 3.5 4.4 4.4l1.7-1.3 2.6 2.3-1.5 2.6C6.6 13.3 2.7 9.4 1 4.2z"/></svg>
        300-555-0142
      </p>
    </div>

    <div class="wordmark">Heronby Mortgage</div>

    <ul class="contact">
      <li class="contact__item">info@heronbymortgage.com
        <svg class="icon" viewBox="0 0 16 16" aria-hidden="true"><path d="M1 3h14v10H1z M2 4.2v.3l6 4.3 6-4.3v-.3z" fill-rule="evenodd"/></svg>
      </li>
      <li class="contact__item">www.heronbymortgage.com
        <svg class="icon" viewBox="0 0 16 16" aria-hidden="true"><circle cx="8" cy="8" r="6.5" fill="none" stroke="#281f55" stroke-width="1.3"/><ellipse cx="8" cy="8" rx="2.8" ry="6.5" fill="none" stroke="#281f55" stroke-width="1.1"/><path d="M1.5 8h13M2.6 5h10.8M2.6 11h10.8" stroke="#281f55" stroke-width="1"/></svg>
      </li>
      <li class="contact__item">00 dummy city, place 0000
        <svg class="icon" viewBox="0 0 16 16" aria-hidden="true"><path d="M8 1a5 5 0 0 1 5 5c0 3.6-5 9-5 9S3 9.6 3 6a5 5 0 0 1 5-5zm0 3a2 2 0 1 0 0 4 2 2 0 0 0 0-4z" fill-rule="evenodd"/></svg>
      </li>
    </ul>
  </section>
</main>
</body>
</html>
```